Business Card: RW Office Partners - Your tidy answer finder

Business Name: RW Office Partners
Website: www.rwofficepartners.com.au
Email: marisol@rwofficepartners.com.au
Mobile: 61 487 902 346
Facebook: @rwofficepartners
Instrgram: @rwofficepartners

Brading Colours:
HEX
#986474
#ddccd3
#7a8498
#c9d8e4
#000000
#ffffff

Tag Line: Your tidy answer finder

Link to DRAFT website:
https://helpdeskhub.sitebuilderx.com/rw-office-partners

About Page from the website:
My name is Marisol Bramwell, and I would love to assist you to become more productive in your day to day and achieve your business and personal goals.
My mission is to give you time, time to work on the important tasks of your business or to be able to spend more time with your family. I will take on the tasks you don’t have time for, don’t know well or simply don’t like to do.
I have an extensive background in Administration, Tender Coordination, Document Control, WHS and Quality Management working primarily in the Construction, Mining and Corporate World.
I am passionate about being organised, having order and making things in your life (and mine) easier! I love to watch something unfold and grow into something amazing! I am known for being the go-to problem solver, the organiser of all things, producing high standards of work even under pressure. I’m also a confident communicator, and I understand that you’re busy running your business.

Target Market(s)

Small to Medium Business who require assistance in their business by a virtual assistant.

Industry/Entity Type

Virtual Assistant

Contact Information for Business Card

Mobile: 61 487 902 346

Font styles to use
Sans Serif

Colors
ffffff

Requirements
Must have
• Branding Colours as outlined.
Contact Details as outlined.
Logo as provided.
Proper contact details - mobile, facebook, instragm, website.
Simple, Elegant, very clean looking.
Should not have
• Note cute with pictures.
Not too girly as still want to market to construction companies.

```html
<!DOCTYPE html>
<html lang="en">
<head>
<meta charset="utf-8">
<title>RW Office Partners – Business Card</title>
<link rel="stylesheet" href="https://fonts.googleapis.com/css2?family=Exo+2:wght@500;600&family=Roboto:wght@400&display=swap">
<style>
  :root {
    --mauve: #8b5f6f;
    --mauve-brand: #986474;
    --blush: #ddccd3;
    --paper: #f5f4f2;
    --ink: #2b2b2b;
    --white: #ffffff;
    --backdrop: #6a6767;
  }
  * { margin: 0; padding: 0; box-sizing: border-box; }
  html, body {
    width: 1200px; height: 1200px; overflow: hidden;
    background: var(--backdrop);
  }
  .stage { position: relative; width: 1200px; height: 1200px; }

  .card {
    position: absolute;
    width: 712px; height: 418px;
    border-radius: 24px;
    overflow: hidden;
  }

  /* Front */
  .card-front {
    left: 238px; top: 118px;
    background: var(--mauve);
    display: flex; align-items: center; justify-content: center;
  }
  .front-name {
    font-family: "Exo 2", sans-serif;
    font-weight: 600;
    font-size: 54px;
    letter-spacing: 1px;
    color: var(--white);
  }

  /* Back */
  .card-back {
    left: 231px; top: 645px;
    background: var(--paper);
  }
  .back-mark {
    position: absolute;
    right: 40px; top: 52px;
    font-family: "Exo 2", sans-serif;
    font-weight: 600;
    font-size: 34px;
    line-height: 1.1;
    text-align: right;
    color: var(--mauve);
  }
  .person { position: absolute; left: 37px; top: 46px; }
  .person-name {
    font-family: "Exo 2", sans-serif;
    font-weight: 600; font-size: 26px;
    color: var(--mauve);
  }
  .person-role {
    font-family: "Roboto", sans-serif;
    font-size: 18px; color: var(--ink);
    margin-top: 2px;
  }
  .company {
    position: absolute; left: 37px; top: 218px;
    font-family: "Exo 2", sans-serif;
    font-weight: 600; font-size: 22px;
    color: var(--mauve);
  }
  .contacts {
    position: absolute; left: 38px; top: 256px;
    list-style: none;
    font-family: "Roboto", sans-serif;
    font-size: 19px; color: var(--ink);
  }
  .contacts li {
    display: flex; align-items: center;
    height: 26px;
  }
  .contacts svg { width: 17px; height: 17px; margin-right: 13px; flex: none; }
  .tagline-band {
    position: absolute; right: 0; bottom: 0;
    width: 360px; height: 50px;
  }
  .tagline {
    position: absolute; right: 34px; bottom: 15px;
    font-family: "Roboto", sans-serif;
    font-size: 18px; color: var(--white);
  }
</style>
</head>
<body>
<main class="stage">

  <section class="card card-front">
    <p class="front-name">RW Office Partners</p>
  </section>

  <section class="card card-back">
    <p class="back-mark">RW Office<br>Partners</p>

    <div class="person">
      <p class="person-name">Marisol Bramwell</p>
      <p class="person-role">Virtual Assistant</p>
    </div>

    <p class="company">RW Office Partners</p>

    <ul class="contacts">
      <li>
        <svg viewBox="0 0 16 16" aria-hidden="true"><path fill="#8b5f6f" d="M2 5c0-2 2-3 6-3s6 1 6 3v1h-3V5H5v1H2zM4 7h8l2 6H2z"/><circle cx="8" cy="10" r="1.6" fill="#f5f4f2"/></svg>
        61 487 902 346
      </li>
      <li>
        <svg viewBox="0 0 16 16" aria-hidden="true"><rect x="1" y="3" width="14" height="10" fill="#8b5f6f"/><path d="M1 3l7 6 7-6" fill="none" stroke="#f5f4f2" stroke-width="1.3"/></svg>
        marisol@rwofficepartners.com.au
      </li>
      <li>
        <svg viewBox="0 0 16 16" aria-hidden="true"><g fill="none" stroke="#8b5f6f" stroke-width="1.3"><circle cx="8" cy="8" r="6.3"/><ellipse cx="8" cy="8" rx="2.7" ry="6.3"/><path d="M1.7 8h12.6M2.8 4.8h10.4M2.8 11.2h10.4"/></g></svg>
        www.rwofficepartners.com.au
      </li>
      <li>
        <svg viewBox="0 0 16 16" aria-hidden="true"><rect x="1.5" y="1.5" width="13" height="13" rx="2" fill="#8b5f6f"/></svg>
        @rwofficepartners
      </li>
      <li>
        <svg viewBox="0 0 16 16" aria-hidden="true"><circle cx="8" cy="8" r="6.5" fill="#8b5f6f"/></svg>
        @rwofficepartners
      </li>
    </ul>

    <svg class="tagline-band" viewBox="0 0 360 50" preserveAspectRatio="none" aria-hidden="true">
      <path d="M28 0H360V50H0Z" fill="#8b5f6f"/>
    </svg>
    <p class="tagline">Your tidy answer finder</p>
  </section>

</main>
</body>
</html>
```